Italian restaurant needs new site

Need to make our website better.

Must have reservation module

Must be able to sell wine tasting tours and wine pairing tours and intégrate with lumo desk

Blog

Social media

Wandermeter ranking and last review.

Number of Pages Required

1 page

Font styles to use
Serif

Requirements
Must have
• Reservation module
• Marketplace to buy wine pairings and gift certificates
• Wandermeter review
• Chatterbay posts
• All info from old site

```html
<!DOCTYPE html>
<html lang="en">
<head>
<meta charset="utf-8">
<title>Vellora Bistro</title>
<link rel="stylesheet" href="https://fonts.googleapis.com/css2?family=Courier+Prime:ital,wght@0,400;0,700;1,400&display=swap">
<style>
  :root {
    --ink: #f2efe9;
    --muted: #b9b4ad;
    --gold: #d9b23a;
    --green: #3fb24a;
    --panel: rgba(0, 0, 0, 0.72);
    --rule: rgba(255, 255, 255, 0.35);
  }
  * { margin: 0; padding: 0; box-sizing: border-box; }
  html, body { width: 1200px; height: 675px; overflow: hidden; background: #000; }
  body { font-family: "Courier Prime", "Courier New", monospace; color: var(--ink); }
  .stage { position: relative; width: 1200px; height: 675px; overflow: hidden; }
  .hero-photo {
    position: absolute; inset: 0;
    background:
      radial-gradient(ellipse at 72% 78%, #b8381c 0%, #8a2614 28%, transparent 60%),
      radial-gradient(ellipse at 78% 30%, #b98a4a 0%, #6e4a28 30%, transparent 62%),
      linear-gradient(135deg, #1a0a0a 0%, #3a1512 45%, #2a0f0c 100%);
  }
  .side-panel {
    position: absolute; left: 0; top: 0; width: 296px; height: 675px;
    background: var(--panel);
    text-align: center;
  }
  .brand { position: absolute; top: 52px; left: 0; width: 100%; }
  .brand-name { color: var(--gold); font-size: 24px; font-weight: 700; letter-spacing: 1px; line-height: 1.1; }
  .brand-tagline { color: var(--gold); font-size: 10px; letter-spacing: 1px; margin-top: 12px; border-top: 1px solid var(--gold); display: inline-block; padding-top: 6px; width: 150px; text-transform: uppercase; }
  .rating-source { position: absolute; top: 190px; left: 0; width: 100%; display: flex; justify-content: center; align-items: center; gap: 6px; font-size: 13px; font-weight: 700; color: var(--ink); }
  .rating-source .dot { width: 12px; height: 12px; border-radius: 50%; background: var(--green); }
  .review-count { position: absolute; top: 221px; left: 0; width: 100%; font-size: 11px; color: var(--muted); letter-spacing: .3px; }
  .ranking { position: absolute; top: 254px; left: 0; width: 100%; font-size: 12.5px; color: var(--green); font-weight: 700; line-height: 15px; }
  .latest-review { position: absolute; top: 331px; left: 0; width: 100%; }
  .latest-review q { font-style: italic; font-size: 17px; letter-spacing: .5px; quotes: "\201C" "\201D"; }
  .latest-review time { display: block; font-size: 11px; color: var(--muted); margin-top: 1px; }
  .review-nav { position: absolute; top: 400px; left: 128px; width: 40px; height: 16px; }
  .divider { position: absolute; top: 443px; left: 49px; width: 197px; border-top: 1px solid var(--rule); }
  .hours { position: absolute; top: 472px; left: 0; width: 100%; font-size: 15.5px; font-weight: 700; letter-spacing: .3px; }
  .reserve-btn { position: absolute; top: 520px; left: 49px; width: 197px; height: 37px; border: 1px solid var(--gold); color: var(--ink); font-family: inherit; font-size: 15px; letter-spacing: 1px; line-height: 35px; background: rgba(0,0,0,.25); }
  .social { position: absolute; top: 610px; left: 0; width: 100%; display: flex; justify-content: center; gap: 14px; font-size: 10px; font-weight: 700; color: var(--ink); }
  .menu-toggle { position: absolute; top: 37px; left: 1147px; }
  .section-dots { position: absolute; left: 1153px; top: 297px; display: flex; flex-direction: column; gap: 11px; }
  .section-dots span { width: 10px; height: 10px; border-radius: 50%; border: 1px solid var(--ink); }
  .section-dots span.active { background: var(--ink); }
  .copyright { position: absolute; right: 41px; top: 645px; font-size: 11px; letter-spacing: .5px; color: var(--ink); }
</style>
</head>
<body>
<div class="stage">
  <div class="hero-photo" role="img" aria-label="Close-up of spaghetti with meatballs in tomato sauce, basil leaf and a glass bowl of garlic bread, with a wine glass in the dark background"></div>

  <aside class="side-panel">
    <div class="brand">
      <div class="brand-name">VELLORA<br>BISTRO</div>
      <div class="brand-tagline">Mediterranean Cuisine</div>
    </div>

    <div class="rating-source"><span class="dot"></span>Wandermeter</div>
    <p class="review-count">Based on 1,086 traveler reviews</p>
    <p class="ranking">#9 of 573 places to eat in<br>Cabo San Lucas</p>

    <div class="latest-review">
      <q>Delicious Italian!</q>
      <time datetime="2017-07-23">Jul 23, 2017</time>
    </div>
    <svg class="review-nav" viewBox="0 0 40 16" aria-label="Review navigation">
      <polyline points="10,3 5,8 10,13" fill="none" stroke="#f2efe9" stroke-width="1.6"/>
      <polyline points="30,3 35,8 30,13" fill="none" stroke="#f2efe9" stroke-width="1.6"/>
    </svg>

    <div class="divider"></div>
    <p class="hours">Open daily from 5 to 12 am</p>
    <div class="reserve-btn">Reserve a table</div>

    <div class="social"><span>Chatterbay</span><span>Wandermeter</span></div>
  </aside>

  <svg class="menu-toggle" width="18" height="15" viewBox="0 0 18 15" aria-label="Menu">
    <rect x="0" y="0" width="18" height="2" fill="#f2efe9"/>
    <rect x="0" y="6.5" width="18" height="2" fill="#f2efe9"/>
    <rect x="0" y="13" width="18" height="2" fill="#f2efe9"/>
  </svg>

  <nav class="section-dots" aria-label="Sections">
    <span class="active"></span><span></span><span></span><span></span>
  </nav>

  <p class="copyright">© Vellora Bistro 2017</p>
</div>
</body>
</html>
```